Bus backs advertising

We need a strong design that can work over a number of messages on the backs of buses.
We are a property investment company.
We need strong, corporate branding. Plus designs that could be translated through to the various bus back specs
Plus could also work on the side of the bus.
Our corporate colours are Black, silver and dark orange.
there are 4 change outs of headlines but All I need is on e strong graphic design at this point
I will attach what I received - which I dont like and I will attach a logo
here is the copy for each variation....
1. Fact #29
You can have
a passive income long before
you retire…..

Find out how
Call 0800 GLIMMER
www.tarvenholdings.co.nz

Logo

2. Fact # 31
It is possible to buy
an investment property
without a cash deposit…

Find out how
Call 0800 GLIMMER

Logo

3. Fact #18
You can have a passive income
Long before
You retire….

Find out how
Call 0800 GLIMMER

Logo

4. Fact #10
Pay for your children’s
Future education without
Cash in the bank…

Find out how
Call 0800 GLIMMER
OR www.tarvenholdings.co.nz

Logo

```html
<!DOCTYPE html>
<html lang="en">
<head>
<meta charset="utf-8">
<title>Tarven Holdings – Bus Back, Fact #34</title>
<link rel="stylesheet" href="https://fonts.googleapis.com/css2?family=Alfa+Slab+One&family=Zilla+Slab:wght@500&family=Nunito:wght@400;800&display=swap">
<style>
  :root {
    --canvas: #000000;
    --bus-body: #4a4a4a;
    --bus-line: #6b6b6b;
    --bus-panel: #707070;
    --silver-light: #f2f2f2;
    --silver-mid: #c9c9c9;
    --silver-dark: #8e8e8e;
    --orange: #f26a21;
    --white: #ffffff;
  }
  html, body {
    margin: 0;
    padding: 0;
    overflow: hidden;
    background: var(--canvas);
  }
  .bus-back {
    position: relative;
    width: 1071px;
    height: 1200px;
    overflow: hidden;
    background: var(--canvas);
  }
  .bus-outline {
    position: absolute;
    inset: 0;
  }
  .fact-number {
    position: absolute;
    left: 70px;
    top: 404px;
    margin: 0;
    font-family: "Alfa Slab One", Georgia, serif;
    font-weight: 400;
    line-height: 0.92;
    text-align: center;
    background: linear-gradient(180deg, var(--silver-light) 0%, var(--silver-mid) 55%, var(--silver-dark) 100%);
    -webkit-background-clip: text;
    background-clip: text;
    color: transparent;
  }
  .fact-number .fact-label { display: block; font-size: 78px; letter-spacing: 2px; }
  .fact-number .fact-digits { display: block; font-size: 104px; letter-spacing: 1px; }
  .headline-rule {
    position: absolute;
    left: 368px;
    top: 214px;
    width: 9px;
    height: 388px;
    border-left: 2px solid var(--orange);
    border-right: 2px solid var(--orange);
    box-sizing: border-box;
  }
  .headline {
    position: absolute;
    left: 396px;
    top: 245px;
    width: 640px;
    margin: 0;
    font-family: "Zilla Slab", Georgia, serif;
    font-weight: 500;
    font-size: 70px;
    line-height: 71px;
    letter-spacing: -0.5px;
    color: var(--silver-mid);
    text-shadow: 2px 3px 4px rgba(0,0,0,0.55);
  }
  .headline .headline-accent { color: var(--orange); }
  .call-to-action {
    position: absolute;
    left: 0;
    width: 1071px;
    top: 680px;
    margin: 0;
    text-align: center;
    font-family: "Nunito", Arial, sans-serif;
    font-weight: 800;
    font-size: 21px;
    letter-spacing: 0.5px;
    color: var(--orange);
  }
  .brand {
    position: absolute;
    left: 0;
    width: 1071px;
    top: 828px;
    display: flex;
    justify-content: center;
    align-items: center;
    gap: 14px;
  }
  .brand-dot {
    width: 34px;
    height: 34px;
    border-radius: 50%;
    background: var(--silver-mid);
  }
  .brand-name {
    font-family: "Nunito", Arial, sans-serif;
    font-weight: 800;
    font-size: 34px;
    letter-spacing: 3px;
    color: var(--silver-mid);
  }
  .contact {
    position: absolute;
    left: 0;
    width: 1071px;
    top: 938px;
    margin: 0;
    text-align: center;
    font-family: "Nunito", Arial, sans-serif;
    font-weight: 400;
    font-size: 23px;
    line-height: 38px;
    color: var(--white);
  }
  .contact strong { font-weight: 800; }
</style>
</head>
<body>
<main class="bus-back">
  <svg class="bus-outline" width="1071" height="1200" viewBox="0 0 1071 1200" aria-hidden="true">
    <rect x="0" y="0" width="1071" height="5" fill="var(--bus-line)"/>
    <!-- bus body -->
    <path d="M36 1200 V200 Q36 110 120 104 Q535 92 951 104 Q1035 110 1035 200 V1200 Z" fill="var(--bus-body)"/>
    <!-- windscreen frame -->
    <path d="M78 626 V230 Q78 140 150 134 Q535 118 921 134 Q993 140 993 230 V626" fill="none" stroke="var(--bus-line)" stroke-width="3"/>
    <path d="M96 626 V240 Q96 158 160 152 Q535 138 911 152 Q975 158 975 240 V626" fill="none" stroke="var(--bus-line)" stroke-width="2"/>
    <circle cx="541" cy="163" r="12" fill="var(--bus-panel)"/>
    <circle cx="139" cy="211" r="26" fill="var(--bus-panel)"/>
    <circle cx="930" cy="211" r="26" fill="var(--bus-panel)"/>
    <rect x="190" y="246" width="197" height="144" fill="var(--bus-panel)"/>
    <!-- lower panel -->
    <path d="M89 1200 V640 Q89 628 101 628 H970 Q982 628 982 640 V1200" fill="none" stroke="var(--bus-line)" stroke-width="3"/>
    <!-- side lamp housings -->
    <path d="M89 797 H60 Q36 797 36 821 V988 Q36 1012 60 1012 H89" fill="none" stroke="var(--bus-line)" stroke-width="3"/>
    <path d="M982 797 H1011 Q1035 797 1035 821 V988 Q1035 1012 1011 1012 H982" fill="none" stroke="var(--bus-line)" stroke-width="3"/>
    <circle cx="75" cy="857" r="24" fill="var(--bus-panel)"/>
    <circle cx="75" cy="952" r="24" fill="var(--bus-panel)"/>
    <circle cx="996" cy="857" r="24" fill="var(--bus-panel)"/>
    <circle cx="996" cy="952" r="24" fill="var(--bus-panel)"/>
    <!-- bumper line and plate -->
    <line x1="89" y1="1020" x2="982" y2="1020" stroke="var(--bus-line)" stroke-width="3"/>
    <rect x="182" y="746" width="292" height="22" fill="var(--bus-panel)"/>
    <rect x="509" y="746" width="60" height="22" fill="var(--bus-panel)"/>
    <rect x="595" y="746" width="290" height="22" fill="var(--bus-panel)"/>
    <rect x="378" y="1030" width="312" height="101" fill="var(--bus-panel)"/>
  </svg>

  <h2 class="fact-number"><span class="fact-label">FACT</span><span class="fact-digits">#34</span></h2>
  <div class="headline-rule"></div>
  <h1 class="headline">It is possible to<br>pay off your<br>mortgage faster,<br><span class="headline-accent">without paying<br>more.</span></h1>

  <p class="call-to-action">FIND OUT HOW AT</p>

  <div class="brand">
    <span class="brand-dot"></span>
    <span class="brand-name">TARVEN HOLDINGS</span>
  </div>

  <p class="contact">www.tarven<strong>holdings</strong>.co.nz<br>or call <strong>0800GLIMMER</strong> today.</p>
</main>
</body>
</html>
```